Fashion Design Business Card

I need a new business card designed for a new fashion company. I have attached what I have currently designed. I want it more feminine looking, the logo needs to be gold. I want it simple, feminine and stylish. Please give me some different ideas with the fonts.
Updates

I need to send the design we currently have, as we have worked out the logo.
You also need all of our details
Industry/Entity Type
Fashion
Look and feel
Each slider illustrates characteristics of the customer's brand and the style your logo design should communicate.

```html
<!DOCTYPE html>
<html lang="en">
<head>
<meta charset="utf-8">
<title>Mila Harwood – Business Card</title>
<link rel="stylesheet" href="https://fonts.googleapis.com/css2?family=Open+Sans:wght@400&family=Gelasio:wght@400&display=swap">
<style>
  :root {
    --ink: #000000;
    --paper: #ffffff;
    --espresso: #2e1a0e;
    --gold: #ffe30f;
    --sans: "Open Sans", sans-serif;
    --serif: "Gelasio", serif;
  }
  * { margin: 0; padding: 0; box-sizing: border-box; }
  html, body { width: 1200px; height: 901px; overflow: hidden; background: var(--paper); }
  .board {
    position: relative; width: 1200px; height: 901px;
    border: 1px solid var(--ink); background: var(--paper);
    font-family: var(--sans); color: var(--ink);
  }
  .side-label {
    position: absolute; font-size: 21px; transform: translateX(-50%);
    font-family: var(--sans);
  }
  .side-label--back { left: 343px; top: 255px; }
  .side-label--front { left: 929px; top: 166px; }

  .card { position: absolute; background: var(--paper); box-shadow: 0 6px 18px rgba(0,0,0,0.12); }
  .card--back { left: 104px; top: 324px; width: 510px; height: 306px; }
  .card--front { left: 771px; top: 220px; width: 306px; height: 509px; }

  .bar { position: absolute; background: var(--espresso); height: 23px; }

  .brand-mark {
    position: absolute; color: var(--gold); font-family: var(--sans);
    text-align: center; line-height: 1.05;
  }
  .brand-mark--small { left: 30px; top: 40px; width: 84px; font-size: 15px; }

  .holder-name {
    position: absolute; left: 127px; top: 53px;
    font-size: 21px; letter-spacing: 0.6px; white-space: nowrap;
  }
  .holder-role {
    position: absolute; left: 126px; top: 84px;
    font-family: var(--serif); font-size: 16px;
  }
  .contact {
    position: absolute; right: 13px; font-family: var(--serif);
    font-size: 16px; white-space: nowrap; text-align: right;
  }

  .front-panel {
    position: absolute; left: 11px; top: 13px; width: 282px; height: 484px;
    background: var(--espresso);
  }
  .brand-mark--large {
    left: 42px; top: 258px; width: 196px; font-size: 38px;
  }
  .front-name {
    position: absolute; left: 0; right: 0; top: 462px;
    text-align: center; color: var(--paper); font-size: 23px; letter-spacing: 0.6px;
  }
</style>
</head>
<body>
<main class="board">
  <p class="side-label side-label--back">back</p>
  <p class="side-label side-label--front">front</p>

  <section class="card card--back" aria-label="Card back">
    <p class="brand-mark brand-mark--small">Mila<br>Harwood</p>
    <p class="holder-name">MILA&nbsp; HARWOOD</p>
    <p class="holder-role">fashion designer</p>
    <div class="bar" style="left:340px; top:52px; width:170px;"></div>

    <div class="bar" style="left:0; top:213px; width:329px;"></div>
    <div class="bar" style="left:0; top:242px; width:187px;"></div>
    <div class="bar" style="left:0; top:271px; width:226px;"></div>

    <p class="contact" style="top:214px;">Phone: 0400123456</p>
    <p class="contact" style="top:243px;">Email:&nbsp; mila@milaharwood.com</p>
    <p class="contact" style="top:272px;">Web:&nbsp; www.milaharwood.com</p>
  </section>

  <section class="card card--front" aria-label="Card front">
    <div class="front-panel">
      <p class="brand-mark brand-mark--large" style="top:245px;">Mila<br>Harwood</p>
      <p class="front-name" style="top:450px;">MILA&nbsp; HARWOOD</p>
    </div>
  </section>
</main>
</body>
</html>
```